Corvane Property Group Business cards

I am starting a property development and consultancy business called Corvane Property Group. I have a logo designed and a website on its way:
www.corvanegroup-example.com.au

I need a business card with the following:

Front:
Mostly orange with logo taking up all front of card

Back of card:
Logo

Mark Dellaway
Managing Director

T +61 452 907 364
E mark.dellaway@corvanegroup-example.com.au
www.corvanegroup-example.com.au

Industry/Entity Type

Business

Requirements
Must have
• curved edges

```html
<!DOCTYPE html>
<html lang="en">
<head>
<meta charset="utf-8">
<title>Corvane Property Group – Business Cards</title>
<link rel="stylesheet" href="https://fonts.googleapis.com/css2?family=Alegreya+Sans+SC:wght@400;500&display=swap">
<style>
  :root {
    --backdrop: #e4e4e4;
    --card-white: #ffffff;
    --brand-orange: #fbab1f;
    --ink: #1c1c1c;
    --shadow: rgba(0, 0, 0, 0.22);
    --card-radius: 18px;
  }
  * { box-sizing: border-box; margin: 0; padding: 0; }
  html, body {
    width: 1200px;
    height: 900px;
    overflow: hidden;
    background: var(--backdrop);
    font-family: "Alegreya Sans SC", sans-serif;
    color: var(--ink);
  }
  .stage {
    position: relative;
    width: 1200px;
    height: 900px;
  }
  .card {
    position: absolute;
    top: 308px;
    width: 514px;
    height: 285px;
    border-radius: var(--card-radius);
    background: var(--card-white);
    overflow: hidden;
    box-shadow: 0 3px 10px var(--shadow);
  }
  .card--front { left: 72px; }
  .card--back  { left: 615px; }

  /* Front */
  .front-band {
    position: absolute;
    left: 0; top: 0;
    width: 100%;
    height: 177px;
    background: var(--brand-orange);
  }
  .front-name {
    position: absolute;
    left: 30px;
    bottom: 118px;
    font-weight: 400;
    font-size: 46px;
    line-height: 1.02;
    color: var(--card-white);
    letter-spacing: 0.02em;
  }

  /* Back */
  .back-band {
    position: absolute;
    left: 0;
    top: 106px;
    width: 228px;
    height: 70px;
    background: var(--brand-orange);
  }
  .back-name {
    position: absolute;
    left: 14px;
    bottom: 8px;
    font-weight: 400;
    font-size: 22px;
    line-height: 1.02;
    color: var(--card-white);
  }
  .person {
    position: absolute;
    left: 248px;
    top: 64px;
  }
  .person-name {
    font-size: 23px;
    font-weight: 500;
    letter-spacing: 0.03em;
    line-height: 1.1;
  }
  .person-role {
    font-size: 12.5px;
    letter-spacing: 0.03em;
    margin-top: 2px;
  }
  .contact {
    position: absolute;
    left: 248px;
    top: 192px;
    list-style: none;
    font-size: 10.5px;
    line-height: 16px;
    letter-spacing: 0.02em;
    white-space: nowrap;
  }
</style>
</head>
<body>
  <main class="stage">
    <section class="card card--front" aria-label="Card front">
      <div class="front-band"></div>
      <p class="front-name">Corvane<br>Property Group</p>
    </section>

    <section class="card card--back" aria-label="Card back">
      <div class="back-band">
        <p class="back-name">Corvane<br>Property Group</p>
      </div>
      <div class="person">
        <h1 class="person-name">Mark Dellaway</h1>
        <p class="person-role">Managing Director</p>
      </div>
      <ul class="contact">
        <li>T +61 452 907 364</li>
        <li>E mark.dellaway@corvanegroup-example.com.au</li>
        <li>www.corvanegroup-example.com.au</li>
      </ul>
    </section>
  </main>
</body>
</html>
```